Business Card Design Project

I am looking for a classy business card design for a product design consultancy. We specialize in Product Design, Prototyping, and Manufacturing Consulting. Products that we design range from consumer electronics to household products all the way to sporting goods. We are based in Arizona and called "Heron Design Works." We like to have fun and goof off as much as we like to create new products. We are young and energetic so we would like our business cards to reflect that. We already have a logo that we would like to implement into the card design. A plain rectangular business card is boring so feel free to get creative, but please, no avocado shaped cards (it's far too literal). Also feel free to play around with textured card stocks or plastic. The final design that we choose will pay attention to all of the little details. Our cards will need to be 2 sided. We're giving you guys free reign to design as you would like. Please have fun with this, it will reflect in our business card.

Thanks guys,
Heron Design Works Team

Industry/Entity Type

Electronics

Requirements
Must have
• We would like to have a spot UV coating somewhere on the business card design if possible.
Nice to have
• Let's see some designs with custom shapes rather than typical rectangular business cards but please no avocado shaped cards, thanks. Also play around with textured card socks.

```html
<!DOCTYPE html>
<html lang="en">
<head>
<meta charset="utf-8">
<title>Heron Design Works – Business Card</title>
<link rel="stylesheet" href="https://fonts.googleapis.com/css2?family=Arimo:wght@400;700&family=Open+Sans:wght@400&display=swap">
<style>
  :root {
    --leaf: #8dc63f;
    --paper: #efefef;
    --ink-grey: #9a9a9a;
    --dot-grey: #a3a3a3;
    --white: #ffffff;
    --halftone-a: #a9b79a;
    --halftone-b: #b3b8ae;
  }
  html, body {
    margin: 0;
    padding: 0;
    width: 1200px;
    height: 684px;
    overflow: hidden;
    background: var(--white);
    font-family: "Arimo", Arial, sans-serif;
  }
  .canvas {
    position: relative;
    width: 1200px;
    height: 684px;
  }
  .card {
    position: absolute;
    width: 530px;
    height: 301px;
    overflow: hidden;
    background: var(--paper);
  }
  /* Front */
  .card--front {
    left: 37px;
    top: 174px;
    border-radius: 23px 0 0 23px;
  }
  .band {
    position: absolute;
    left: 0;
    width: 100%;
    background: var(--leaf);
  }
  .band--top { top: 0; height: 80px; }
  .band--bottom { top: 211px; height: 90px; }
  .halftone {
    position: absolute;
    left: 49px;
    width: 434px;
    border-radius: 6px;
    background: linear-gradient(90deg, var(--halftone-a), var(--halftone-b) 50%, var(--halftone-a));
    opacity: 0.85;
  }
  .halftone--top { top: 9px; height: 60px; }
  .halftone--bottom { top: 226px; height: 67px; }
  .brand {
    position: absolute;
    left: 40px;
    top: 80px;
    height: 131px;
    display: flex;
    align-items: center;
    gap: 16px;
  }
  .brand__mark {
    width: 40px;
    height: 40px;
    border-radius: 50%;
    background: var(--leaf);
  }
  .brand__name {
    font-family: "Arimo", Arial, sans-serif;
    font-weight: 400;
    font-size: 40px;
    color: var(--leaf);
    letter-spacing: 0.5px;
  }
  /* Back */
  .card--back {
    left: 631px;
    top: 176px;
    border-radius: 0 23px 23px 0;
  }
  .band--name { top: 83px; height: 131px; }
  .row {
    position: absolute;
    display: flex;
    align-items: center;
    color: var(--ink-grey);
  }
  .row__label {
    font-family: "Arimo", Arial, sans-serif;
    font-size: 17px;
    width: 71px;
  }
  .row__dot {
    width: 10px;
    height: 10px;
    border-radius: 50%;
    background: var(--dot-grey);
    margin-right: 12px;
  }
  .row__value { font-size: 12px; }
  .row--email { left: 44px; top: 20px; }
  .row--web { left: 44px; top: 44px; }
  .row--phone { left: 52px; top: 247px; }
  .row--phone .row__label { width: 71px; }
  .row--phone .row__value { font-weight: 700; font-size: 12.5px; margin-right: 42px; }
  .person {
    position: absolute;
    left: 75px;
    top: 83px;
    height: 131px;
    display: flex;
    align-items: center;
    color: var(--white);
  }
  .person__name {
    font-family: "Arimo", Arial, sans-serif;
    font-weight: 700;
    font-size: 37px;
  }
  .person__title {
    font-family: "Open Sans", Arial, sans-serif;
    font-size: 27px;
    margin-left: 12px;
  }
  .person__title::before {
    content: "•";
    margin-right: 10px;
  }
</style>
</head>
<body>
<main class="canvas">
  <section class="card card--front" aria-label="Card front">
    <div class="band band--top">
      <div class="halftone halftone--top" role="img" aria-label="Grey halftone dot pattern"></div>
    </div>
    <div class="brand">
      <span class="brand__mark"></span>
      <span class="brand__name">Heron Design Works</span>
    </div>
    <div class="band band--bottom" style="top:211px">
    </div>
    <div class="halftone halftone--bottom" role="img" aria-label="Grey halftone dot pattern"></div>
  </section>

  <section class="card card--back" aria-label="Card back">
    <div class="row row--email">
      <span class="row__label">Email</span>
      <span class="row__dot"></span>
      <span class="row__value">dylan@herondesignworks.com</span>
    </div>
    <div class="row row--web">
      <span class="row__label">Web</span>
      <span class="row__dot"></span>
      <span class="row__value">www.herondesignworks.com</span>
    </div>
    <div class="band band--name"></div>
    <div class="person">
      <span class="person__name">Dylan Marsh</span>
      <span class="person__title">President</span>
    </div>
    <div class="row row--phone">
      <span class="row__label">Phone</span>
      <span class="row__dot"></span>
      <span class="row__value">Office: 480.555.0143</span>
      <span class="row__dot"></span>
      <span class="row__value">Cell: 602.555.0178</span>
    </div>
  </section>
</main>
</body>
</html>
```